Business Card Design

I need a business card for my rental business. The business is named:
Cruise a Trikeway Houston
www.cruiseatrikewayhouston.com
(832) 555-0193
This will be a business card that I will leave at other businesses as advertisement so it needs to have the name, website, and phone number.
Please feel free to be creative. This is a new business so I have no designs.
Thank you very much for your time and I look forward to receiving your designs
Target Market(s)
Local rental customers
Industry/Entity Type
Business
Contact Information for Business Card
Please check out my website:
Font styles to use
Other font styles liked:
- anything creative
Colors
Designer to choose colors to be used in the design.
Requirements
Must have
- Business name, phone, website. Rentals available hourly or daily. Book online

```html
<!DOCTYPE html>
<html lang="en">
<head>
<meta charset="utf-8">
<title>Cruise a Trikeway Houston – Business Card</title>
<link rel="stylesheet" href="https://fonts.googleapis.com/css2?family=Lato:wght@300;400;700;900&display=swap">
<style>
  :root {
    --page-bg: #2a2a2a;
    --card-top: #242424;
    --card-bottom: #151515;
    --logo-grey: #c4c4c4;
    --logo-grey-dim: #8e8e8e;
    --text-light: #d6d6d6;
    --text-muted: #707070;
    --rule: #7a7a7a;
    --band: #5c5c5c;
    --band-dark: #2c2c2c;
  }
  * { margin: 0; padding: 0; box-sizing: border-box; }
  html, body { width: 1200px; height: 900px; overflow: hidden; }
  body {
    background: var(--page-bg);
    font-family: "Lato", sans-serif;
    position: relative;
  }
  .card {
    position: absolute;
    width: 640px;
    height: 365px;
    border-radius: 22px;
    overflow: hidden;
    background: linear-gradient(160deg, var(--card-top), var(--card-bottom));
    box-shadow: 0 18px 40px rgba(0,0,0,0.55);
  }
  .card--front { left: 80px; top: 50px; }
  .card--back { left: 480px; top: 485px; }

  .brand-name {
    font-family: "Lato", sans-serif;
    font-weight: 900;
    text-transform: uppercase;
    letter-spacing: 1.5px;
    color: var(--logo-grey);
    white-space: nowrap;
  }

  .front-lockup {
    position: absolute;
    left: 0; right: 0; top: 140px;
    text-align: center;
  }
  .front-lockup .brand-name { font-size: 36px; }
  .front-lockup .brand-url {
    display: block;
    text-align: right;
    margin: 4px 50px 0 0;
    font-size: 13px;
    color: var(--text-muted);
    letter-spacing: 0.3px;
  }

  .back-brand {
    position: absolute;
    right: 34px; top: 36px;
    text-align: right;
  }
  .back-brand .brand-name { font-size: 25px; color: var(--logo-grey-dim); }
  .back-tagline {
    margin-top: 8px;
    font-size: 13px;
    font-weight: 400;
    color: var(--text-muted);
    letter-spacing: 0.4px;
  }

  .card-band {
    position: absolute;
    left: 0; top: 0;
    width: 640px; height: 365px;
  }

  .holder {
    position: absolute;
    left: 46px; top: 130px;
  }
  .holder-name {
    font-size: 28px;
    font-weight: 400;
    color: var(--text-light);
  }
  .holder-title {
    font-size: 15px;
    font-weight: 300;
    color: var(--text-muted);
    margin-top: 2px;
  }
  .holder-rule {
    width: 150px;
    height: 2px;
    background: var(--rule);
    margin-top: 22px;
  }

  .contact-list {
    position: absolute;
    left: 46px; top: 240px;
    list-style: none;
  }
  .contact-item {
    display: flex;
    align-items: center;
    gap: 12px;
    font-size: 15px;
    color: var(--text-light);
    font-weight: 400;
    height: 26px;
  }
  .contact-item svg { width: 16px; height: 16px; flex: none; }
</style>
</head>
<body>

  <section class="card card--front" aria-label="Card front">
    <div class="front-lockup">
      <span class="brand-name">Cruise a Trikeway Houston</span>
      <span class="brand-url">www.cruiseatrikewayhouston.com</span>
    </div>
  </section>

  <section class="card card--back" aria-label="Card back">
    <svg class="card-band" viewBox="0 0 640 365" aria-hidden="true">
      <polygon points="480,230 640,230 640,365 480,365" fill="var(--band-dark)"/>
      <polygon points="0,340 470,340 500,262 640,262 640,365 0,365" fill="var(--band)"/>
    </svg>

    <div class="back-brand">
      <span class="brand-name">Cruise a Trikeway Houston</span>
      <p class="back-tagline">Rentals available hourly or daily. Book online</p>
    </div>

    <div class="holder">
      <div class="holder-name">Your Name</div>
      <div class="holder-title">job Title</div>
      <div class="holder-rule"></div>
    </div>

    <ul class="contact-list">
      <li class="contact-item">
        <svg viewBox="0 0 16 16" aria-hidden="true"><path d="M8 1a5 5 0 0 0-5 5c0 3.6 5 9 5 9s5-5.4 5-9a5 5 0 0 0-5-5zm0 7a2 2 0 1 1 0-4 2 2 0 0 1 0 4z" fill="#8c8c8c"/></svg>
        FM-1180, Houston, Texas 77090, United States
      </li>
      <li class="contact-item">
        <svg viewBox="0 0 16 16" aria-hidden="true"><path d="M2 5.5C2 3.5 5 2.5 8 2.5s6 1 6 3v1.2h-3V5.3H5v1.4H2zM4 7.5h8l1.8 5.5H2.2z" fill="#8c8c8c"/></svg>
        (832) 555-0193
      </li>
      <li class="contact-item">
        <svg viewBox="0 0 16 16" aria-hidden="true" fill="none" stroke="#8c8c8c" stroke-width="1.2"><circle cx="8" cy="8" r="6.3"/><ellipse cx="8" cy="8" rx="2.8" ry="6.3"/><path d="M1.7 8h12.6M2.8 4.8h10.4M2.8 11.2h10.4"/></svg>
        www.cruiseatrikewayhouston.com
      </li>
    </ul>
  </section>

</body>
</html>
```